Kelbrook Aquatic Centre Open Day

FRONT PAGE

KELBROOK AQUATIC CENTRE OPEN DAY
31st May 2014
10am - 4pm
Free entry

Our Free Open Day is an event designed for the community to dive in and enjoy our great aquatic venue. There are plenty of activities for parents and kids to enjoy including the pool activities, free fitness classes and much more! Come join us on this great day to mark our 6 months of operation.

Sausage sizzle
pool activities
free group fitness classes
giveaways
door prizes

BACK PAGE
map of location
ph: 4731 5082
enquiries@kbaquatic-demo.com.au

want fitness and aquatic pics

plenty of colour - DL size
in your face kind of flyer

```html
<!DOCTYPE html>
<html lang="en">
<head>
<meta charset="utf-8">
<title>Kelbrook Aquatic Centre Open Day</title>
<link rel="stylesheet" href="https://fonts.googleapis.com/css2?family=Russo+One&family=Nunito:wght@800;900&family=Roboto+Condensed:wght@400&family=Roboto:wght@400&display=swap">
<style>
  :root {
    --sky: #c4e1ee;
    --sky-stripe: #d6ebf4;
    --grey-stripe: #e3e6e8;
    --band-blue: #8fc3d8;
    --orange: #f2661c;
    --orange-text: #f06a1f;
    --navy: #1d3f63;
    --teal-text: #1b5d7c;
    --charcoal: #3a3a3a;
    --logo-teal: #3db4cb;
    --white: #ffffff;
  }
  * { margin: 0; padding: 0; box-sizing: border-box; }
  html, body { width: 1200px; height: 1000px; overflow: hidden; }
  body { background: var(--white); }

  .flyer {
    position: relative;
    width: 1200px;
    height: 1000px;
    overflow: hidden;
    background:
      repeating-linear-gradient(-35deg, var(--sky) 0 48px, var(--sky-stripe) 48px 80px),
      var(--sky);
  }
  .flyer::after {
    content: "";
    position: absolute;
    left: 0; right: 0; bottom: 0; height: 520px;
    background: linear-gradient(to bottom, rgba(227,230,232,0), var(--grey-stripe) 70%);
    opacity: .75;
    pointer-events: none;
  }

  .bands { position: absolute; inset: 0; z-index: 1; }

  .logo-box {
    position: absolute;
    left: 503px; top: 33px;
    width: 296px; height: 137px;
    background: var(--white);
    z-index: 3;
    display: flex;
    align-items: center;
    justify-content: center;
    text-align: center;
  }
  .logo-name {
    font-family: "Nunito", sans-serif;
    font-weight: 900;
    font-size: 38px;
    line-height: 1.05;
    color: var(--logo-teal);
    letter-spacing: 1px;
  }

  .photo {
    position: absolute;
    z-index: 2;
    box-shadow: 2px 3px 6px rgba(0,0,0,.35);
  }
  .photo--polo {
    left: 308px; top: 104px; width: 266px; height: 190px;
    transform: rotate(6deg);
    background: linear-gradient(160deg, #6fd0e6, #1c96c2 60%, #0f6f9a);
  }
  .photo--gym {
    left: 97px; top: 262px; width: 244px; height: 162px;
    transform: rotate(-5deg);
    background: linear-gradient(180deg, #c8c6bf, #8a8780 55%, #5e5b55);
    z-index: 3;
  }
  .photo--trainer {
    left: 545px; top: 208px; width: 268px; height: 190px;
    transform: rotate(-6deg);
    background: linear-gradient(135deg, #f4f4f4, #e2e2e2 55%, #b9b9b9);
    z-index: 3;
  }
  .photo--swimmer {
    left: 822px; top: 130px; width: 262px; height: 168px;
    transform: rotate(-3deg);
    background: linear-gradient(160deg, #bfe9f6, #45b6df 55%, #1f8cc0);
  }

  .venue-title {
    position: absolute;
    left: 295px; top: 418px;
    z-index: 3;
    font-family: "Roboto", sans-serif;
    font-size: 27px;
    color: var(--navy);
    letter-spacing: .5px;
  }

  .headline {
    position: absolute;
    left: 348px; top: 468px;
    z-index: 3;
    font-family: "Russo One", sans-serif;
    font-size: 76px;
    color: var(--charcoal);
    letter-spacing: 3px;
  }

  .free-entry {
    position: absolute;
    left: 52px; top: 552px;
    width: 256px; height: 150px;
    z-index: 3;
  }
  .free-entry svg { position: absolute; inset: 0; width: 100%; height: 100%; }
  .free-entry span {
    position: absolute; inset: 0;
    display: flex; align-items: center; justify-content: center;
    font-family: "Roboto Condensed", sans-serif;
    font-size: 46px;
    color: var(--white);
  }

  .intro {
    position: absolute;
    left: 390px; top: 594px;
    width: 680px;
    z-index: 3;
    font-family: "Nunito", sans-serif;
    font-weight: 800;
    font-size: 26.5px;
    line-height: 30px;
    letter-spacing: 1.6px;
    color: var(--teal-text);
  }

  .highlights {
    position: absolute;
    left: 42px; top: 772px;
    z-index: 3;
    list-style: none;
    font-family: "Nunito", sans-serif;
    font-weight: 800;
    font-size: 23px;
    line-height: 33px;
    letter-spacing: 1px;
    color: var(--orange-text);
  }

  .when {
    position: absolute;
    left: 742px; top: 770px;
    z-index: 3;
    transform: rotate(-8deg);
    transform-origin: left top;
    font-family: "Roboto", sans-serif;
    font-size: 54px;
    line-height: 70px;
    color: var(--orange-text);
  }
</style>
</head>
<body>
<main class="flyer">

  <svg class="bands" width="1200" height="1000" viewBox="0 0 1200 1000" aria-hidden="true">
    <polygon points="0,0 890,0 860,22 0,22" fill="var(--orange)"/>
    <polygon points="0,88 470,88 440,140 0,140" fill="var(--orange)"/>
    <polygon points="0,140 440,140 420,175 0,175" fill="#9fcde0" opacity=".7"/>
    <polygon points="0,180 330,180 300,215 0,215" fill="var(--orange)"/>
    <polygon points="1035,40 1200,40 1200,70 1005,70" fill="#5b9bb5" opacity=".6"/>
    <polygon points="1080,110 1200,110 1200,128 1068,128" fill="#5b9bb5" opacity=".6"/>
    <polygon points="1070,228 1110,228 1098,246 1058,246" fill="var(--orange)"/>
    <polygon points="0,390 110,390 80,425 0,425" fill="#5b9bb5" opacity=".55"/>
    <polygon points="945,460 1030,460 1052,575 975,575" fill="var(--orange)"/>
    <polygon points="108,450 940,450 1000,568 150,568" fill="var(--band-blue)"/>
    <polygon points="150,568 1000,568 1010,578 160,578" fill="var(--orange)"/>
    <polygon points="185,970 1000,970 980,1000 205,1000" fill="var(--orange)"/>
  </svg>

  <div class="logo-box">
    <p class="logo-name">KELBROOK<br>AQUATIC CENTRE</p>
  </div>

  <div class="photo photo--polo" role="img" aria-label="Water polo player raising a ball in the pool"></div>
  <div class="photo photo--gym" role="img" aria-label="Trainer coaching a client in the gym"></div>
  <div class="photo photo--trainer" role="img" aria-label="Personal trainer helping a member lift a dumbbell"></div>
  <div class="photo photo--swimmer" role="img" aria-label="Swimmer doing freestyle laps"></div>

  <h2 class="venue-title">KELBROOK AQUATIC CENTRE</h2>
  <h1 class="headline">OPEN DAY</h1>

  <div class="free-entry">
    <svg viewBox="-1 -1 2 2" preserveAspectRatio="none" aria-hidden="true">
      <polygon fill="var(--orange)" points="1,0 .853,.112 .966,.259 .795,.329 .866,.5 .682,.524 .707,.707 .524,.682 .5,.866 .329,.795 .259,.966 .112,.853 0,1 -.112,.853 -.259,.966 -.329,.795 -.5,.866 -.524,.682 -.707,.707 -.682,.524 -.866,.5 -.795,.329 -.966,.259 -.853,.112 -1,0 -.853,-.112 -.966,-.259 -.795,-.329 -.866,-.5 -.682,-.524 -.707,-.707 -.524,-.682 -.5,-.866 -.329,-.795 -.259,-.966 -.112,-.853 0,-1 .112,-.853 .259,-.966 .329,-.795 .5,-.866 .524,-.682 .707,-.707 .682,-.524 .866,-.5 .795,-.329 .966,-.259 .853,-.112"/>
    </svg>
    <span>Free Entry</span>
  </div>

  <p class="intro">There are plenty of activities for parents and kids to enjoy including the pool activities, free fitness classes and much more! Come join us on this great day to mark our 6 months of operation.</p>

  <ul class="highlights">
    <li>Sausage sizzle</li>
    <li>pool activities</li>
    <li>free group fitness classes</li>
    <li>giveaways</li>
    <li>door prizes</li>
  </ul>

  <p class="when">31st May 2014<br>10am - 4pm</p>

</main>
</body>
</html>
```